Tintmarble app graphic design
Graphics and layout of our Tintmarble app
Project: Tintmarble app graphic design
Tintmarble app graphic design - Photography
Creative Brief
Photography
www.brightvole.net
This software allows the user to easily change a color photo to a black and white photo with colored areas. No photo editing experience necessary. This project is the Tintmarble app version of the software. We need a design layout/template of the app. The canvas area will need to stay the same size, it is what it is, so use that as a starting point. The controls can be moved a bit, but only if necessary. Everything else you can design how you see fit, including the graphics behind the controls. Obviously, the goal is to make this app look appealing and friendly so users will want to use it. I will explain the different sections of the app in the additional comments section.
Like the black and white and use of different bold colors / gradients.
Colorful
Soft
left side
http://apps.tintmarble.example/huepickerbench/
The link to the live app is provided in the referred websites section. Also, see our main website www.brightvole.net for reference. Starting with the canvas area (diagonal lines) and build from there. The canvas is 640x530. We will provide the logo to incorporate above the canvas and control section. The tagline is "Easily change your photos from Color... to Black & White AND Color!" Below the app we need the following sections: A chart comparing features / benefits of this version and the full version. Has a click here to save $10 off full version An area to advertise the website PrintsOnSlate.example with a click here to save 20% off all products. An area to place a banner ad of general size that will rotate different banners. An area to pitch the photo contest that users can enter when they edit their photos in Hue Picker Bench Lite.
lumtavo lumtavo
karvel904: we like #11 and #12. The red headers and buttons are great. Instead of using that red in every location could you incorporate a couple of other colors? For instance, one is red, one blue, one green or yellow. (keeping the same bold values)
karvel904 - great design! Use less pink and a white background. Recommend using different bold colors.
Also, we prefer white background. Please see this link: http://www.layoutorca.example/shopkit-themes/58172.html The bold colors on the dark grey area really stand out. If you could incorporate this type of design it would be best.
Hello everyone. Thanks for the designs already submitted. I just uploaded an image, example.jpg, that shows how to layout the design. The green areas are the areas to concentrate on.
delmoraxx delmoraxx
Sir your brief do not have a proper idea...too many constants adds..give me the proper layout ..Thanks.
PlumtreeArtwork PlumtreeArtwork
can you give me the proper layout of app in what ever format so that i can get idea proper alignment of gui kit in app
Sir, I am working in on that.thanks.
SiteAdmin SiteAdmin
Attention Designers, Our policy for stock photos has changed and is effective immediately. QuillVantor does not recommend the use of stock images. However, if you are submitting a design that uses a stock image (ex: website design) it is mandatory to provide the source of the image. Please provide the source in the comment section when uploading. Logos and stationery should NEVER use stock and/or clipart images. Any draft not following these guidelines will be withdrawn. Thanks, QV/RTK Team

```html
<!DOCTYPE html>
<html lang="en">
<head>
<meta charset="utf-8">
<title>Hue Picker Bench Lite – Tintmarble app</title>
<link rel="stylesheet" href="https://fonts.googleapis.com/css2?family=Arimo:wght@400;700&display=swap">
<style>
  :root {
    --bar-blue: #3b5998;
    --bar-dark: #29447e;
    --strip: #ffffff;
    --night: #040a1c;
    --glow-blue: #1c4fd6;
    --glow-cyan: #5fb8ff;
    --ember: #d2472a;
    --amber: #f2a23a;
    --pink: #ff4fb6;
    --panel: #f3f3f3;
    --panel-edge: #c9c9c9;
    --button: #1f3fbf;
    --ink: #1d1d1d;
    --muted: #6b6b6b;
    --white: #ffffff;
    --red: #e5322d;
    --photo-light: #bdbdbd;
    --photo-dark: #7a7f86;
  }
  * { box-sizing: border-box; margin: 0; padding: 0; }
  html, body { width: 1200px; height: 814px; overflow: hidden; background: var(--white); }
  body { position: relative; font-family: "Arimo", Arial, sans-serif; color: var(--ink); }

  .network-bar { position: absolute; left: 0; top: 0; width: 1200px; height: 24px; background: var(--bar-blue); border-bottom: 1px solid var(--bar-dark); }
  .network-name { position: absolute; left: 166px; top: 3px; color: var(--white); font-weight: 700; font-size: 16px; }
  .network-search { position: absolute; left: 270px; top: 4px; width: 230px; height: 16px; background: var(--white); border: 1px solid var(--bar-dark); }

  .like-strip { position: absolute; left: 0; top: 24px; width: 1200px; height: 24px; background: var(--strip); }
  .like-button { position: absolute; left: 575px; top: 5px; font-size: 9px; padding: 1px 4px; background: #eceef5; border: 1px solid #cad4e7; color: var(--bar-blue); font-weight: 700; }
  .like-count { position: absolute; left: 610px; top: 7px; font-size: 9px; color: var(--bar-blue); }

  .stage {
    position: absolute; left: 0; top: 48px; width: 1200px; height: 766px;
    background:
      radial-gradient(ellipse 260px 200px at 150px 740px, rgba(242,162,58,.55), transparent 70%),
      radial-gradient(ellipse 300px 180px at 470px 780px, rgba(210,71,42,.6), transparent 70%),
      radial-gradient(ellipse 260px 160px at 1010px 740px, rgba(210,71,42,.35), transparent 70%),
      radial-gradient(ellipse 240px 360px at 980px 170px, rgba(95,184,255,.35), transparent 70%),
      radial-gradient(ellipse 520px 460px at 600px 300px, rgba(28,79,214,.65), transparent 75%),
      linear-gradient(180deg, #061233 0%, var(--night) 60%, #120812 100%);
  }

  .brand { position: absolute; left: 365px; top: 54px; width: 176px; height: 30px; display: flex; align-items: center; gap: 6px; background: #0b0f25; border: 1px solid #2a3160; padding: 0 8px; }
  .brand-dot { width: 10px; height: 10px; border-radius: 50%; background: var(--pink); }
  .brand-name { color: var(--pink); font-weight: 700; font-size: 13px; white-space: nowrap; }

  .tagline { position: absolute; left: 576px; top: 52px; width: 290px; color: var(--white); font-weight: 700; font-size: 15px; line-height: 17px; }
  .tagline .hue { color: var(--pink); }

  .controls { position: absolute; left: 365px; top: 106px; width: 74px; height: 333px; background: linear-gradient(180deg, #1a2350, #0b1030); border: 1px solid #3a4a8c; padding: 4px 4px; color: var(--white); font-size: 8px; }
  .step-label { background: var(--button); text-align: center; font-size: 10px; padding: 2px 0; margin-bottom: 4px; letter-spacing: 1px; }
  .control-button { background: var(--white); color: var(--button); font-weight: 700; font-size: 10px; text-align: center; border-radius: 3px; padding: 6px 2px; margin-bottom: 10px; line-height: 12px; }
  .hint { text-align: center; line-height: 10px; margin-bottom: 8px; }
  .slider { position: relative; height: 20px; margin: 4px 2px 2px; }
  .slider-track { position: absolute; left: 0; right: 0; top: 9px; height: 2px; background: #9aa3c9; }
  .slider-knob { position: absolute; left: 40px; top: 3px; width: 14px; height: 14px; border-radius: 50%; background: var(--white); }
  .slider-label { text-align: center; margin-bottom: 12px; }
  .option { display: flex; align-items: center; gap: 4px; margin-bottom: 5px; white-space: nowrap; }
  .radio { width: 8px; height: 8px; border-radius: 50%; border: 1px solid var(--white); flex: none; }
  .radio.on { background: var(--white); }
  .controls .save { margin-top: 32px; }

  .canvas-frame { position: absolute; left: 444px; top: 106px; width: 396px; height: 292px; background: var(--panel); border: 1px solid var(--panel-edge); padding: 26px 22px 22px; }
  .canvas-photo { width: 100%; height: 100%; background: linear-gradient(160deg, var(--photo-light), var(--photo-dark)); }

  .compare { position: absolute; left: 365px; top: 439px; width: 475px; height: 118px; display: flex; }
  .version { padding: 10px 12px; position: relative; }
  .version.lite { width: 266px; background: linear-gradient(180deg, #d7dcea, #8e9cc4); }
  .version.full { width: 209px; background: linear-gradient(180deg, #1a1a1a, #3a0d0d); }
  .lite-mark { position: absolute; left: 12px; top: 14px; width: 40px; height: 88px; background: var(--bar-blue); }
  .version h3 { font-size: 14px; font-weight: 700; margin-left: 48px; margin-bottom: 8px; }
  .version.lite h3 { color: var(--bar-blue); }
  .version.full h3 { margin-left: 0; color: var(--white); }
  .version.full h3 span { color: var(--red); }
  .version ul { list-style: none; font-size: 9px; line-height: 13px; }
  .version.lite ul { margin-left: 56px; color: var(--bar-dark); }
  .version.full ul { color: #e6e6e6; }
  .version li::before { content: "\2022"; margin-right: 5px; color: var(--red); }
  .version.lite li::before { color: var(--bar-blue); }
  .save-note { font-size: 9px; color: var(--white); margin-top: 4px; white-space: nowrap; }
  .save-note b { color: var(--red); }

  .contest { position: absolute; left: 365px; top: 566px; width: 271px; height: 111px; background: linear-gradient(180deg, #141414, #000); padding: 12px 10px; color: var(--white); }
  .contest p { width: 150px; font-size: 11px; line-height: 14px; }
  .contest .accent { color: var(--amber); font-weight: 700; }
  .contest .product { color: var(--glow-cyan); font-weight: 700; }
  .contest-button { display: inline-block; margin-top: 8px; background: var(--white); color: var(--ink); font-size: 9px; padding: 3px 8px; font-weight: 700; }
  .contest-photo { position: absolute; right: 8px; top: 8px; width: 96px; height: 95px; background: linear-gradient(160deg, #f0d9b5, #c98a4a 60%, #5a3a22); }

  .ad-slot { position: absolute; left: 643px; top: 566px; width: 197px; height: 207px; background: var(--white); border: 1px solid var(--panel-edge); padding: 4px 6px; }
  .ad-label { font-size: 8px; color: var(--muted); margin-bottom: 4px; }
  .ad-art { height: 150px; background: linear-gradient(160deg, #eef4fb, #9cb9dc 55%, #2a5d9f); }
  .ad-copy { font-size: 10px; color: #2a5d9f; font-weight: 700; margin-top: 10px; text-align: right; }

  .slate-promo { position: absolute; left: 324px; top: 680px; width: 312px; height: 93px; background: linear-gradient(180deg, #101010, #000); color: var(--white); }
  .slate-photo { position: absolute; left: 8px; top: 8px; width: 44px; height: 77px; background: linear-gradient(180deg, #9ecbe8, #3b6b8f); }
  .slate-brand { position: absolute; left: 64px; top: 10px; display: flex; align-items: center; gap: 6px; }
  .slate-square { width: 12px; height: 12px; background: var(--glow-cyan); }
  .slate-name { font-size: 18px; font-weight: 700; color: var(--white); }
  .slate-line { position: absolute; left: 64px; top: 38px; font-size: 9px; color: #cfcfcf; }
  .slate-offer { position: absolute; left: 64px; top: 62px; font-size: 12px; font-weight: 700; }
  .slate-offer b { color: var(--glow-cyan); }
</style>
</head>
<body>
  <header class="network-bar">
    <span class="network-name">Tintmarble</span>
    <span class="network-search"></span>
  </header>
  <div class="like-strip">
    <span class="like-button">Like</span>
    <span class="like-count">845,621 people like this app</span>
  </div>

  <main class="stage" role="img" aria-label="Dark blue background with vertical light streaks and warm bokeh glow"></main>

  <div class="brand"><span class="brand-dot"></span><span class="brand-name">Hue Picker Bench V 2.0</span></div>
  <p class="tagline">Easily change your photos from <span class="hue">Color...</span><br>to Black &amp; White AND Color!</p>

  <aside class="controls">
    <div class="step-label">STEP 1</div>
    <div class="control-button">Open<br>Photo</div>
    <div class="step-label">STEP 2</div>
    <p class="hint">Click areas to bring color back</p>
    <div class="slider"><span class="slider-track"></span><span class="slider-knob"></span></div>
    <p class="slider-label">Cursor Size</p>
    <div class="option"><span class="radio on"></span>Add Color</div>
    <div class="option"><span class="radio"></span>Remove Color</div>
    <div class="option"><span class="radio"></span>Reset Color</div>
    <div class="control-button save">Save<br>Photo</div>
  </aside>

  <section class="canvas-frame">
    <div class="canvas-photo" role="img" aria-label="Editing canvas showing a black and white photo with one area kept in color"></div>
  </section>

  <section class="compare">
    <div class="version lite">
      <span class="lite-mark"></span>
      <h3>Tintmarble version</h3>
      <ul>
        <li>Basic color select tools</li>
        <li>Save photos up to 800px</li>
        <li>Share edits with friends</li>
      </ul>
    </div>
    <div class="version full">
      <h3><span>FULL</span> version</h3>
      <ul>
        <li>Advanced color select tools</li>
        <li>Save photos at full size</li>
        <li>Unlimited undo and redo</li>
        <li>Batch editing</li>
      </ul>
      <p class="save-note">click <b>HERE</b> to save $10 off full version</p>
    </div>
  </section>

  <section class="contest">
    <p>Enter Our <span class="accent">Photo Contest</span> when editing your photos with <span class="product">Hue Picker Bench Lite</span></p>
    <span class="contest-button">enter the contest</span>
    <div class="contest-photo" role="img" aria-label="Photo of a person holding a camera"></div>
  </section>

  <section class="ad-slot">
    <p class="ad-label">Commercial</p>
    <div class="ad-art" role="img" aria-label="Rotating banner ad showing a laptop"></div>
    <p class="ad-copy">New slim laptop from $599</p>
  </section>

  <section class="slate-promo">
    <div class="slate-photo" role="img" aria-label="Photo printed on a translucent panel"></div>
    <div class="slate-brand"><span class="slate-square"></span><span class="slate-name">PrintsOnSlate.example</span></div>
    <p class="slate-line">Your Favorite Photos Printed on Translucent Glass</p>
    <p class="slate-offer">click <b>HERE</b> to save $20 off all products</p>
  </section>
</body>
</html>
```